Bref créative
Quillmont Care Associates
Business Cards & Stationary
Bright & Fun-filled
Harold J. Mabbery, Ph.D.
Co-founder
4815 North Larkin Road
Vista, CA 92083
drhmabbery@examplemail.net
Licensed Psychologist PSY58706
On the front of the card, we would like to see some versions with the logos symbol.
This business card is for a California Board Licensed Psychologist.
The look of this should be professional, but because it is for therapy, we would like it to be professional with a hint of:
* warm and welcoming
* serenity, tranquility and happiness
* positive, future, growth
On the back of the business card please place the:
1. Logo symbol and company name
2. Child, Adolescence, Family, Adult Therapy
logo
We need to see how the back of a card looks with the Quillmont Care Logo and the following information attached.

```html
<!DOCTYPE html>
<html lang="en">
<head>
<meta charset="utf-8">
<title>Quillmont Care Associates — Stationery Set</title>
<link href="https://fonts.googleapis.com/css2?family=Cinzel:wght@600&family=Open+Sans:wght@400;600&display=swap" rel="stylesheet">
<style>
:root{
  --ground:#ece9e4;
  --paper:#ffffff;
  --blue:#2f8fd6;
  --blue-soft:#cfe5f6;
  --grey:#6d6f73;
  --ink:#3a3d42;
  --muted:#8a8d92;
  --shadow:0 2px 6px rgba(0,0,0,.18);
}
*{box-sizing:border-box;margin:0;padding:0}
html,body{width:1200px;height:446px;overflow:hidden}
body{background:var(--ground);font-family:"Open Sans",sans-serif;color:var(--ink);position:relative}
.piece{position:absolute;background:var(--paper);box-shadow:var(--shadow);overflow:hidden}
.label{position:absolute;font-size:6px;letter-spacing:.18em;text-transform:uppercase;color:var(--muted)}
.brand{display:flex;flex-direction:column;align-items:center;gap:2px}
.brand-dot{width:14px;height:14px;border-radius:50%;background:var(--blue)}
.brand-name{font-family:"Cinzel",serif;font-weight:600;color:var(--blue);font-size:6px;letter-spacing:.06em;text-align:center;line-height:1.2}
.faint-circle{position:absolute;border-radius:50%;background:var(--blue-soft);opacity:.45}
.band{position:absolute;left:0;right:0;bottom:0;background:var(--blue)}
.small{font-size:4px;line-height:1.5;color:var(--grey)}

/* business cards */
.card-front{left:19px;top:151px;width:125px;height:77px}
.card-front .brand{position:absolute;left:8px;top:10px}
.card-front .details{position:absolute;right:8px;top:10px;text-align:left}
.card-front .band{height:6px}
.card-back{left:19px;top:257px;width:125px;height:72px}
.card-back .brand{position:absolute;left:0;right:0;top:16px}
.card-back .services{position:absolute;left:0;right:0;top:50px;text-align:center}
.card-back .band{height:4px}

/* letterheads */
.letterhead{top:7px;width:293px;height:415px}
.lh-1{left:163px}
.lh-2{left:475px}
.letterhead .band{height:10px}
.lh-1 .brand{position:absolute;left:24px;top:22px}
.lh-1 .contact{position:absolute;right:60px;top:24px}
.lh-2 .brand{position:absolute;left:0;right:0;top:22px}
.letterhead .footer{position:absolute;left:0;right:0;bottom:14px;text-align:center}
.letterhead .faint-circle{width:120px;height:120px;right:40px;bottom:50px}
.lh-2 .faint-circle{right:auto;left:86px;bottom:150px}

/* envelopes */
.envelope{left:792px;width:391px;height:98px}
.env-blue{top:10px}
.env-grey{top:120px}
.env-white{top:230px}
.envelope svg{position:absolute;inset:0}
.env-front{left:792px;top:343px;width:276px;height:84px}
.env-front .brand{position:absolute;left:14px;top:12px}
.env-front .band{height:5px}
</style>
</head>
<body>

<div class="label" style="left:19px;top:125px">Stationary Design</div>

<section class="piece card-front">
  <div class="brand"><span class="brand-dot"></span><span class="brand-name">Quillmont<br>Care</span></div>
  <div class="details small">
    <strong style="color:var(--ink)">Harold J. Mabbery, Ph.D.</strong><br>
    Co-founder<br>
    4815 North Larkin Road<br>
    Vista, CA 92083<br>
    drhmabbery@examplemail.net<br>
    Licensed Psychologist PSY58706
  </div>
  <div class="band"></div>
</section>
<div class="label" style="left:19px;top:240px">Business Card Front</div>

<section class="piece card-back">
  <div class="brand"><span class="brand-dot"></span><span class="brand-name">Quillmont Care Associates</span></div>
  <p class="services small">Child, Adolescence, Family, Adult Therapy</p>
  <div class="band"></div>
</section>
<div class="label" style="left:19px;top:341px">Business Card Back</div>

<section class="piece letterhead lh-1">
  <div class="brand"><span class="brand-dot"></span><span class="brand-name">Quillmont Care<br>Associates</span></div>
  <div class="contact small">
    4815 North Larkin Road<br>
    Vista, CA 92083<br>
    (760) 555-0187<br>
    drhmabbery@examplemail.net
  </div>
  <div class="faint-circle"></div>
  <div class="band"></div>
</section>
<div class="label" style="left:268px;top:432px">Letterhead Option 1</div>

<section class="piece letterhead lh-2">
  <div class="brand"><span class="brand-dot"></span><span class="brand-name">Quillmont Care<br>Associates</span></div>
  <div class="faint-circle"></div>
  <p class="footer small">4815 North Larkin Road · Vista, CA 92083 · (760) 555-0187 · www.quillmontcare.example</p>
  <div class="band"></div>
</section>
<div class="label" style="left:580px;top:432px">Letterhead Option 2</div>

<section class="piece envelope env-blue">
  <svg viewBox="0 0 391 98" preserveAspectRatio="none" aria-hidden="true">
    <rect width="391" height="98" fill="var(--paper)"/>
    <path d="M0 0H391V34Q196 70 0 34Z" fill="var(--blue)"/>
    <circle cx="196" cy="40" r="6" fill="var(--paper)"/>
  </svg>
</section>
<section class="piece envelope env-grey">
  <svg viewBox="0 0 391 98" preserveAspectRatio="none" aria-hidden="true">
    <rect width="391" height="98" fill="var(--paper)"/>
    <path d="M0 0H391V34Q196 70 0 34Z" fill="var(--grey)"/>
    <circle cx="196" cy="40" r="6" fill="var(--paper)"/>
  </svg>
</section>
<section class="piece envelope env-white">
  <svg viewBox="0 0 391 98" preserveAspectRatio="none" aria-hidden="true">
    <rect width="391" height="98" fill="var(--paper)"/>
    <path d="M0 0H391V34Q196 70 0 34Z" fill="#f7f8fa" stroke="#d9dbde"/>
    <circle cx="196" cy="40" r="6" fill="var(--blue)"/>
  </svg>
</section>
<section class="piece env-front">
  <div class="brand"><span class="brand-dot"></span><span class="brand-name">Quillmont Care<br>Associates</span></div>
  <div class="band"></div>
</section>
<div class="label" style="left:1100px;top:432px">Envelope Design</div>

</body>
</html>
```